Brightwell Consulting Business Card Design

Business Card Design for Brightwell Consulting. Brightwell Consulting is a boutique consultancy based in Atlanta, GA., that specializes in marketing strategy, organization planning, and leadership development. We provide solutions for small businesses and startups as well as Summit 400 companies.

http://brightwellconsulting.example/

Target Market(s)

We provide solutions for small businesses and startups as well as Summit 400 companies.

Industry/Entity Type

Consulting

Contact Information for Business Card

Two sided business card with priority on contact information, logo, tag line (Inspiration to Dream More, Do More, Become More)

Colors

Designer to choose colors to be used in the design.

Requirements
Must have
• contact information, logo, tag line (Inspiration to Dream More, Do More, Become More)
• Simple no over communication.
Nice to have
• I would like to see different placements of logo and creative use of both sides of the card
Should not have
• Do not put too much information on the card.

```html
<!DOCTYPE html>
<html lang="en">
<head>
<meta charset="utf-8">
<title>Brightwell Consulting — Business Card</title>
<link rel="stylesheet" href="https://fonts.googleapis.com/css2?family=Lato:wght@300;700&display=swap">
<style>
  :root {
    --paper: #ffffff;
    --ink: #1e1e1e;
    --rule: #555555;
    --photo-light: #a9aeb2;
    --photo-mid: #80868b;
    --photo-dark: #5d6266;
    --on-photo: #ffffff;
  }
  * { margin: 0; padding: 0; box-sizing: border-box; }
  html, body {
    width: 1051px; height: 1200px; overflow: hidden;
    background: var(--paper);
    font-family: "Lato", Arial, sans-serif;
  }
  .card { position: relative; width: 1051px; height: 1200px; background: var(--paper); }

  .hero {
    position: absolute; left: 0; top: 0; width: 1051px; height: 600px;
    background: linear-gradient(160deg, var(--photo-light) 0%, var(--photo-mid) 50%, var(--photo-dark) 100%);
  }
  .tagline {
    position: absolute; left: 42px; top: 52px;
    border-left: 3px solid var(--on-photo);
    padding-left: 16px;
    color: var(--on-photo);
    font-weight: 700; font-size: 45px; line-height: 54px;
    text-transform: uppercase; letter-spacing: 0;
  }
  .brand-name {
    position: absolute; left: 48px; top: 470px;
    color: var(--on-photo);
    font-weight: 300; font-size: 40px; letter-spacing: 4px;
    text-transform: uppercase;
  }

  .about {
    position: absolute; left: 45px; top: 652px;
    border-left: 2px solid var(--rule);
    padding-left: 16px;
    color: var(--ink);
    font-weight: 300; font-size: 33px; line-height: 41px;
    text-transform: uppercase;
  }

  .contact {
    position: absolute; right: 99px; top: 1056px;
    text-align: right; color: var(--ink);
    font-weight: 300; font-size: 38px; font-style: normal;
  }
  .contact .phone { padding-right: 8px; line-height: 46px; }
  .contact .email { line-height: 50px; }
</style>
</head>
<body>
<main class="card">
  <section class="hero" role="img" aria-label="Photograph of a grey woven architectural facade">
    <h1 class="tagline">Inspiration to dream more,<br>do more, become more</h1>
    <p class="brand-name">Brightwell Consulting</p>
  </section>

  <p class="about">We are a boutique consultancy<br>based in Atlanta, GA.</p>

  <address class="contact">
    <div class="phone">404-555-0187</div>
    <div class="email">hello@brightwellconsulting.example</div>
  </address>
</main>
</body>
</html>
```